Poster Design Project- New Years Eve

We are a fun and quirky bar in St Kilda (www.coppernook.com.au). We need a poster designed for our New Years Eve Event- details as follows
Project: A1 poster-NYE
Name of Event: Lucky Comets
Date of Event: New Years Eve: 31.12.12
Tagline: ‘What happens at Nook stays at Nook’
Time: 8pm-3am
Cost:
$105 all inclusive
-Includes a cocktail on arrival
-4 hour drink package – Basic Spirits, Premium Beer, Wine and Sparkling til 12AM
-Grazing style canapés and finger food
Early bird and group discounts (10+) available
Purchase your tickets at the bar or through the website
Dress: For Fun and Dancing
Venue information:
• Address: 14 Harwell Lane St Kilda
• Phone: 9413 6057
• Email: info@coppernook.com.au
• Website: www.coppernook.com.au
• Management reserves the right to refuse entry
Images: Images need to be high resolution or vector images so clarity is not lost when the poster is blown up to this size
Poster production:
Poster needs to be created in either Adobe Illustrator or Photoshop so we can easily edit the details if they change after the contest ends
Please provide 3mm internal and external bleed
Theming:
Fun poster with elements of Las Vegas including: dice/casino element, Las Lucky Comets, pretty girls, cocktails
Target Market(s)
25-40 year olds
Industry/Entity Type
Casino

```html
<!DOCTYPE html>
<html lang="en">
<head>
<meta charset="utf-8">
<title>Lucky Comets – New Years Eve Poster</title>
<link rel="stylesheet" href="https://fonts.googleapis.com/css2?family=Bungee&family=Righteous&family=Yellowtail&family=Montserrat:wght@700;800&display=swap">
<style>
  :root {
    --page: #e9e9e9;
    --gold: #f2c81a;
    --gold-deep: #c98a0a;
    --ink: #07070c;
    --cyan: #2fd8ff;
    --magenta: #ff4fd8;
    --pink: #ff66c4;
    --yellow: #ffe22a;
    --red: #e0102a;
    --blue: #1746c8;
    --white: #ffffff;
  }
  * { box-sizing: border-box; margin: 0; padding: 0; }
  html, body { width: 1200px; height: 848px; overflow: hidden; background: var(--page); }
  .poster {
    position: absolute; left: 315px; top: 24px; width: 570px; height: 800px;
    background: var(--gold); padding: 9px;
    box-shadow: 0 4px 14px rgba(0,0,0,.25);
  }
  .poster-inner {
    position: relative; width: 100%; height: 100%; background: var(--ink); overflow: hidden;
    font-family: "Montserrat", sans-serif; font-weight: 800; text-transform: uppercase;
  }
  .artwork { position: absolute; inset: 0; }
  .glow-frame {
    position: absolute; inset: 12px; border: 3px solid var(--cyan);
    box-shadow: 0 0 12px var(--cyan), inset 0 0 12px var(--cyan);
  }
  .price-badge {
    position: absolute; left: 58px; top: 28px; width: 150px; height: 150px; border-radius: 50%;
    background: radial-gradient(circle, #3a3a44 0%, #111 70%); border: 4px solid #222;
    box-shadow: 0 0 0 2px #555; text-align: center; transform: rotate(-12deg);
  }
  .price-badge .amount { font-family: "Bungee", sans-serif; font-size: 44px; color: var(--yellow); margin-top: 36px; line-height: 1; text-shadow: 2px 2px 0 #6a3a00; }
  .price-badge .note { font-size: 14px; color: var(--yellow); margin-top: 4px; }
  .venue-name {
    position: absolute; left: 236px; top: 48px; width: 300px;
    font-family: "Righteous", sans-serif; font-size: 36px; color: var(--yellow); text-transform: none;
    display: flex; align-items: center; gap: 10px;
  }
  .venue-name .dot { width: 14px; height: 14px; border-radius: 50%; background: var(--yellow); }
  .hours { position: absolute; left: 388px; top: 108px; font-size: 17px; color: var(--yellow); }
  .date-row { position: absolute; left: 92px; top: 168px; display: flex; gap: 22px; }
  .date-row span {
    width: 42px; height: 42px; border-radius: 50%; background: var(--yellow);
    border: 4px solid var(--blue); box-shadow: 0 0 0 2px var(--white);
    font-family: "Bungee", sans-serif; font-size: 22px; color: var(--red);
    display: flex; align-items: center; justify-content: center;
  }
  .event-eyebrow { position: absolute; top: 216px; width: 100%; text-align: center; font-family: "Righteous", sans-serif; font-size: 15px; color: var(--red); letter-spacing: 2px; }
  .event-title { position: absolute; top: 232px; width: 100%; text-align: center; font-family: "Bungee", sans-serif; font-size: 84px; line-height: 1; color: #7fe9ff; -webkit-text-stroke: 2px #0a2a7a; text-shadow: 0 0 14px var(--cyan); }
  .event-script { position: absolute; top: 306px; width: 100%; text-align: center; font-family: "Yellowtail", cursive; font-size: 64px; line-height: 1; color: var(--red); text-transform: none; text-shadow: 2px 2px 0 #fff, 0 0 10px var(--magenta); }
  .tagline { position: absolute; top: 404px; width: 100%; text-align: center; font-family: "Righteous", sans-serif; font-size: 27px; line-height: 1.22; color: var(--yellow); text-shadow: 2px 2px 0 #5a2a00; }
  .details { position: absolute; left: 0; top: 502px; width: 100%; text-align: center; }
  .dress { position: absolute; right: 36px; top: 0; font-size: 8px; color: var(--cyan); }
  .inclusions { margin-top: 18px; font-size: 12.5px; line-height: 1.55; }
  .inclusions .pink { color: var(--pink); }
  .inclusions .gold { color: var(--yellow); }
  .inclusions .magenta { color: var(--magenta); font-weight: 700; }
  .offers { margin-top: 6px; font-family: "Righteous", sans-serif; font-size: 13px; line-height: 1.3; color: var(--yellow); }
  .venue-info { margin-top: 8px; list-style: none; color: var(--cyan); }
  .venue-info .heading { font-size: 7.5px; margin-bottom: 3px; }
  .venue-info li.item { font-size: 13px; line-height: 1.45; }
  .venue-info li.item::before { content: "•"; margin-right: 14px; }
  .venue-info .small { font-size: 7px; color: var(--white); }
</style>
</head>
<body>
<main class="poster">
  <div class="poster-inner">
    <svg class="artwork" viewBox="0 0 552 782" preserveAspectRatio="none" aria-hidden="false">
      <defs>
        <radialGradient id="burst" cx="50%" cy="28%" r="75%">
          <stop offset="0" stop-color="#ffd34a"/>
          <stop offset=".3" stop-color="#b8541c"/>
          <stop offset=".65" stop-color="#2b1410"/>
          <stop offset="1" stop-color="#07070c"/>
        </radialGradient>
        <linearGradient id="city" x1="0" y1="0" x2="0" y2="1">
          <stop offset="0" stop-color="#1a1208" stop-opacity="0"/>
          <stop offset=".5" stop-color="#3a2410"/>
          <stop offset="1" stop-color="#0d0a10"/>
        </linearGradient>
        <linearGradient id="sign" x1="0" y1="0" x2="0" y2="1">
          <stop offset="0" stop-color="#ffe98a"/>
          <stop offset="1" stop-color="#d89a18"/>
        </linearGradient>
        <linearGradient id="ribbon" x1="0" y1="0" x2="0" y2="1">
          <stop offset="0" stop-color="#ffb020"/>
          <stop offset="1" stop-color="#b85a06"/>
        </linearGradient>
      </defs>
      <g role="img" aria-label="Fireworks bursting over a night city skyline">
        <rect width="552" height="782" fill="url(#burst)"/>
        <rect y="400" width="552" height="382" fill="url(#city)"/>
      </g>
      <g role="img" aria-label="Las Vegas style marquee sign with dice, poker chips, stars and a ribbon banner">
        <ellipse cx="276" cy="290" rx="250" ry="105" fill="url(#sign)" opacity=".9"/>
        <path d="M40 395 L512 395 L490 430 L512 465 L40 465 L62 430 Z" fill="url(#ribbon)"/>
        <path d="M150 465 L276 500 L402 465 Z" fill="#d88a10"/>
      </g>
    </svg>
    <div class="glow-frame"></div>

    <div class="price-badge"><p class="amount">$105</p><p class="note">All Inclusive</p></div>
    <div class="venue-name"><span class="dot"></span>Copper Nook</div>
    <p class="hours">8pm-3am</p>

    <div class="date-row"><span>3</span><span>1</span><span>1</span><span>2</span><span>1</span><span>2</span></div>

    <p class="event-eyebrow">New Years Eve</p>
    <h1 class="event-title">Lucky</h1>
    <p class="event-script">Comets</p>
    <p class="tagline">What happens at Nook<br>stays at Nook</p>

    <section class="details">
      <p class="dress">Dress: For fun and dancing</p>
      <div class="inclusions">
        <p class="pink">Includes a cocktail on arrival</p>
        <p class="gold">4 hour drink package</p>
        <p class="magenta">Basic spirits, premium beer, wine and sparkling til 12AM</p>
        <p class="pink">Grazing style canapés and finger food</p>
      </div>
      <div class="offers">
        <p>Early bird and group discounts (10+) available</p>
        <p>Purchase your tickets at the bar or through the website</p>
      </div>
      <ul class="venue-info">
        <li class="heading">Venue information:</li>
        <li class="item">Address: 14 Harwell Lane St Kilda</li>
        <li class="item">Phone: 9413 6057</li>
        <li class="item">Email: info@coppernook.com.au</li>
        <li class="item">Website: www.coppernook.com.au</li>
        <li class="small">• Management reserves the right to refuse entry</li>
      </ul>
    </section>
  </div>
</main>
</body>
</html>
```